Business Podcaster needs a sexy book cover design for upcoming book launch

I'm launching a book called Find Your Mentor: how to accelerate your growth through reaching out, getting a response from, and leaving an impression on the people you admire most. It would be cool to have maybe a band of heroes or a single hero or something on the cover, then I'll need the spine designed, as well as the back cover which would be mostly just quotes about the book from other prominent people.

I dont want to extend it. I want to shorten it. Can I do that?

```html
<!DOCTYPE html>
<html lang="en">
<head>
<meta charset="UTF-8">
<title>Find Your Mentor – Book Cover Wrap</title>
<link href="https://fonts.googleapis.com/css2?family=Dosis:wght@300;400;500&display=swap" rel="stylesheet">
<style>
  :root {
    --page: #ffffff;
    --back-bg: #ede8e5;
    --ink: #1f1f22;
    --body-ink: #2a2a2a;
    --spine-red: #b3201a;
    --title-red: #b8231a;
    --sky-top: #8497a6;
    --sky-mid: #c9cdcf;
    --glow: #f3dcc0;
    --sun: #e78a3a;
    --rock: #2b2220;
    --skin-light: #e9bf9a;
    --skin-dark: #9a5a34;
    --white: #ffffff;
  }
  * { margin: 0; padding: 0; box-sizing: border-box; }
  html, body {
    width: 1200px; height: 1200px; overflow: hidden;
    background: var(--page);
    font-family: "Dosis", sans-serif;
  }
  .wrap {
    position: absolute; left: 0; top: 164px;
    width: 1200px; height: 868px;
  }
  /* Back cover */
  .back-cover {
    position: absolute; left: 0; top: 0; width: 566px; height: 868px;
    background: var(--back-bg);
    overflow: hidden;
  }
  .back-blurb {
    position: absolute; left: 68px; top: 80px; width: 438px;
    font-weight: 300; font-size: 16px; line-height: 31.2px;
    color: var(--body-ink); text-align: justify;
  }
  .back-blurb .lead { font-size: 32px; font-weight: 400; line-height: 1; }
  .handshake-photo {
    position: absolute; left: 0; top: 505px; width: 566px; height: 280px;
    background: linear-gradient(100deg, var(--skin-dark) 0%, #b97448 35%, var(--skin-light) 70%, #f1d2b6 100%);
    border-radius: 40% 40% 30% 30% / 50% 50% 40% 40%;
    opacity: 0.85;
  }
  .isbn-box {
    position: absolute; left: 358px; top: 718px; width: 186px; height: 114px;
    background: var(--white);
  }
  /* Spine */
  .spine {
    position: absolute; left: 566px; top: 0; width: 66px; height: 868px;
    background: var(--spine-red);
  }
  .spine-title, .spine-author {
    position: absolute; left: 50%; white-space: nowrap; color: var(--ink);
    transform-origin: 0 0;
  }
  .spine-title {
    top: 46px; font-size: 40px; font-weight: 400;
    transform: translateX(18px) rotate(90deg);
  }
  .spine-author {
    top: 528px; font-size: 19px; font-weight: 400; letter-spacing: 0.68em;
    color: var(--white);
    transform: translateX(10px) rotate(90deg);
  }
  /* Front cover */
  .front-cover {
    position: absolute; left: 632px; top: 0; width: 568px; height: 868px;
    overflow: hidden;
  }
  .hero-photo {
    position: absolute; inset: 0;
    background:
      radial-gradient(ellipse 60% 30% at 62% 78%, var(--sun) 0%, rgba(231,138,58,0.4) 40%, rgba(0,0,0,0) 75%),
      linear-gradient(180deg, var(--sky-top) 0%, var(--sky-mid) 45%, var(--glow) 70%, #7a4a34 86%, var(--rock) 100%);
  }
  .front-title { position: absolute; left: 0; top: 0; }
  .subtitle {
    position: absolute; left: 0; width: 568px; top: 282px;
    text-align: center; font-size: 23px; font-weight: 500;
    line-height: 23.6px; color: var(--ink); letter-spacing: 0.02em;
  }
  .front-author {
    position: absolute; left: 0; width: 568px; top: 812px;
    text-align: center; font-size: 27px; font-weight: 400;
    letter-spacing: 0.72em; color: var(--white); padding-left: 0.72em;
  }
</style>
</head>
<body>
  <div class="wrap">
    <section class="back-cover">
      <p class="back-blurb"><span class="lead">Lorem ipsum</span> dolor sit amet, consectetur adipiscing elit, sed do eiusmod tempor incididunt ut labore et dolore magna aliqua. Ut enim ad minim veniam, quis nostrud exercitation ullamco laboris nisi ut aliquip ex ea commodo consequat. Duis aute irure dolor in reprehenderit in voluptate velit esse cillum dolore eu fugiat nulla pariatur. Excepteur sint occaecat cupidatat non proident, sunt in culpa qui officia deserunt mollit anim id est laborum.<br>Lorem ipsum dolor sit amet, consectetur adipiscing elit, sed do eiusmod tempor incididunt ut labore et dolore magna aliqua. Ut enim ad minim veniam, quis nostrud exercitation ullamco laboris nisi ut aliquip ex ea commodo consequat. Duis aute irure dolor in reprehenderit in voluptate velit esse cillum dolore eu fugiat nulla pariatur.</p>
      <div class="handshake-photo" role="img" aria-label="Photo of two hands clasped in a handshake"></div>
      <div class="isbn-box"></div>
    </section>

    <section class="spine">
      <div class="spine-title">FIND YOUR MENTOR</div>
      <div class="spine-author">AUTHOR NAME</div>
    </section>

    <section class="front-cover">
      <div class="hero-photo" role="img" aria-label="Photo of a man in a suit and red cape standing on a hilltop at sunset, seen from behind"></div>
      <svg class="front-title" width="568" height="290" viewBox="0 0 568 290">
        <text x="78" y="124" font-family="Dosis, sans-serif" font-size="98" font-weight="400" fill="#1f1f22" textLength="408" lengthAdjust="spacingAndGlyphs">FIND YOUR</text>
        <text x="80" y="268" font-family="Dosis, sans-serif" font-size="186" font-weight="400" fill="#b8231a" textLength="410" lengthAdjust="spacingAndGlyphs">MENTOR</text>
      </svg>
      <p class="subtitle">How to accelerate your growth through<br>reaching out, getting a response from,<br>and leaving an impression on the<br>people you admire most</p>
      <div class="front-author">AUTHOR NAME</div>
    </section>
  </div>
</body>
</html>
```